The Queen Rides Again Line of Sparkling Wine & Spirits

Back info: Tara Joy Whitfield Owner 209-555-0143 1700 E. Harlowe Rd, Bldg. 2, & 3, Lodi Ca. 95111
Sparkling Wines & Memorabilia www.thequeenridesagain.example
Ok I have uploaded the winning design. The color that I am after is the Fushia, Raspberry, Red, Matte Satin Matalic Finish. With a 24 Karet Gold color Foil. The Bottle is on the top row and it's the 2nd Bottle in. That is the Color that I want. This is the style of font. Make sure that you put what we're advertising. Good Luck to you all. Warmest regards, Tara
Target Market(s)
21 & up UniSex
Industry/Entity Type
Sparkling Wine and Memorabilia
Contact Information for Business Card
there listed up above.....
Look and feel

```html
<!DOCTYPE html>
<html lang="en">
<head>
<meta charset="utf-8">
<title>The Queen Rides Again – Business Card</title>
<link rel="stylesheet" href="https://fonts.googleapis.com/css2?family=Arimo:wght@400;700&display=swap">
<style>
  :root {
    --canvas: #e4e4e4;
    --paper: #ffffff;
    --fuchsia-deep: #9c1256;
    --fuchsia: #e0168e;
    --gold: #f2d06a;
    --gold-rule: #8a5a1c;
    --ink: #1a1a1a;
    --grey-dark: #5a5a5a;
    --white: #ffffff;
  }
  * { margin: 0; padding: 0; box-sizing: border-box; }
  html, body {
    width: 1200px; height: 1200px; overflow: hidden;
    background: var(--canvas);
    font-family: "Arimo", Arial, sans-serif;
  }
  .card {
    position: absolute;
    left: 266px;
    width: 688px;
    height: 393px;
    background: var(--paper);
    overflow: hidden;
  }
  .card--front { top: 159px; }
  .card--back {
    top: 653px;
    background: linear-gradient(to bottom, var(--paper) 0%, var(--paper) 48%, #e6e6e6 62%, #a3a3a3 80%, var(--grey-dark) 100%);
    border-bottom: 2px solid var(--fuchsia);
  }
  .bottle {
    position: absolute;
    border-radius: 12px 12px 8px 8px;
    background: linear-gradient(to right, var(--fuchsia-deep), var(--fuchsia) 45%, var(--fuchsia-deep));
  }
  .card--front .bottle { left: 316px; top: 27px; width: 53px; height: 177px; }
  .card--back .bottle { left: 308px; top: 57px; width: 69px; height: 242px; }

  .gold-rule {
    position: absolute; left: 0; top: 230px; width: 100%; height: 6px;
    background: linear-gradient(to right, #6e4415, var(--gold-rule) 50%, #6e4415);
  }
  .contact-band {
    position: absolute; left: 0; top: 237px; width: 100%; height: 156px;
    background: linear-gradient(to right, var(--fuchsia-deep) 0%, var(--fuchsia) 50%, var(--fuchsia-deep) 100%);
    color: var(--white);
  }
  .name-line {
    position: absolute; left: 0; width: 100%; top: 32px;
    text-align: center; white-space: nowrap;
  }
  .name { color: var(--gold); font-weight: 700; font-size: 26px; }
  .slash { color: var(--gold); font-size: 26px; margin: 0 6px; }
  .role { font-size: 18px; }
  .address {
    position: absolute; right: 363px; top: 78px;
    text-align: right; font-size: 16.5px; line-height: 21px;
  }
  .divider {
    position: absolute; left: 341px; top: 79px; width: 1px; height: 49px;
    background: var(--white);
  }
  .reach { position: absolute; left: 360px; top: 78px; font-size: 16.5px; line-height: 21px; }
  .reach li { list-style: none; display: flex; align-items: center; gap: 8px; }
  .reach svg { width: 15px; height: 15px; flex: none; }

  .base-line {
    position: absolute; left: 148px; top: 300px; width: 403px; height: 1px;
    background: linear-gradient(to right, transparent, #444 20%, #444 80%, transparent);
  }
  .tagline {
    position: absolute; left: 0; width: 100%; top: 326px;
    text-align: center; font-size: 18px; letter-spacing: 4.4px; color: var(--ink);
  }
  .tagline strong { font-weight: 700; }
</style>
</head>
<body>
  <section class="card card--front">
    <div class="bottle" role="img" aria-label="Fuchsia sparkling wine bottle with gold neck band"></div>
    <div class="gold-rule"></div>
    <div class="contact-band">
      <p class="name-line"><span class="name">TARA JOY WHITFIELD</span><span class="slash">/</span><span class="role">Owner</span></p>
      <p class="address">1700 E. Harlowe Rd<br>Bldg. 2, &amp; 3, Lodi Ca. 95111</p>
      <div class="divider"></div>
      <ul class="reach">
        <li>
          <svg viewBox="0 0 24 24"><path fill="#f2d06a" d="M6.6 10.8a15.1 15.1 0 0 0 6.6 6.6l2.2-2.2c.3-.3.7-.4 1-.2 1.1.4 2.3.6 3.6.6.6 0 1 .4 1 1V20c0 .6-.4 1-1 1A17 17 0 0 1 3 4c0-.6.4-1 1-1h3.5c.6 0 1 .4 1 1 0 1.3.2 2.5.6 3.6.1.3 0 .7-.2 1z"/></svg>
          209-555-0143
        </li>
        <li>
          <svg viewBox="0 0 24 24"><circle cx="12" cy="12" r="10" fill="#f2d06a"/><path fill="none" stroke="#b8125f" stroke-width="1.4" d="M2 12h20M12 2c3 3 3 17 0 20M12 2c-3 3-3 17 0 20"/></svg>
          www.thequeenridesagain.example
        </li>
      </ul>
    </div>
  </section>

  <section class="card card--back">
    <div class="bottle" role="img" aria-label="Fuchsia sparkling wine bottle with gold neck band"></div>
    <div class="base-line"></div>
    <p class="tagline">SPARKLING <strong>WINES &amp; MEMORABILIA</strong></p>
  </section>
</body>
</html>
```